Simple, clean boat charter Banners

We need a variety of banner designs for our charter boat company. We provide boat trips to marlow shoals, beaches and snorkeling. You can see our site www.velmarotrips.com to get a better idea of our image.

We need the banner to be clean, simple and pleasing to the eye. The following ad dimensions we need are:

300 x 250
336 x 280
728 x 90
300 x 600
320 x 100

I've included a range of photos and logos to pic from.

Ignore the logo in all the photos. If a portion of the logo in the photo is in the banner, down worry. I will proved photos with the logo removed for the winning designs.

Please include a phrase, such as the following:
- Private Boat Charters to Marlow Shoals
- Private Boat Charters in Grand Cayman

If you can think of fun witty phrases, feel free to try them out. We are very open to creative ideas!! For example:
- Come visit the stingrays with us!
- Have you ever kissed a stingray?

Target Market(s)

Up-scale 30-50 year olds residing in North America

Industry/Entity Type

Tourism

Colors
3176b5
0655a3
85cae6
33a6d7
0592cd
cee9f5

Requirements
Nice to have
• Clean, Simple, Modern

```html
<!DOCTYPE html>
<html lang="en">
<head>
<meta charset="utf-8">
<title>Velmaro Trips – Private Boat Charters in Grand Cayman</title>
<link rel="stylesheet" href="https://fonts.googleapis.com/css2?family=Cinzel:wght@600&display=swap">
<style>
  :root {
    --deep-blue: #0655a3;
    --navy: #0b2f6e;
    --ocean: #0592cd;
    --lagoon: #33a6d7;
    --sky: #85cae6;
    --foam: #cee9f5;
    --white: #ffffff;
  }
  html, body {
    margin: 0;
    padding: 0;
    width: 1200px;
    height: 148px;
    overflow: hidden;
    background: var(--white);
  }
  .banner {
    position: relative;
    width: 1200px;
    height: 148px;
    overflow: hidden;
    font-family: "Cinzel", "Times New Roman", serif;
  }
  .underwater-scene {
    position: absolute;
    inset: 0;
    background:
      radial-gradient(ellipse 260px 120px at 220px 40px, rgba(206,233,245,0.55), transparent 70%),
      radial-gradient(ellipse 320px 140px at 1050px 60px, rgba(5,146,205,0.5), transparent 70%),
      linear-gradient(180deg, var(--lagoon) 0%, var(--ocean) 55%, var(--deep-blue) 100%);
  }
  .brand {
    position: absolute;
    left: 26px;
    top: 80px;
    display: flex;
    align-items: center;
    gap: 10px;
    color: var(--white);
    font-weight: 600;
  }
  .brand-dot {
    width: 12px;
    height: 12px;
    border-radius: 50%;
    background: var(--white);
  }
  .brand-name {
    font-size: 30px;
    letter-spacing: 2px;
    line-height: 1;
  }
  .brand-name small {
    display: block;
    font-size: 12px;
    letter-spacing: 5px;
    text-align: center;
    margin-top: 4px;
  }
  .headline-badge {
    position: absolute;
    left: 606px;
    top: -52px;
    width: 252px;
    height: 252px;
    border-radius: 50%;
    background: var(--navy);
    border: 3px solid var(--white);
    box-sizing: border-box;
  }
  .headline {
    position: absolute;
    left: 606px;
    top: 0;
    width: 252px;
    height: 148px;
    margin: 0;
    display: flex;
    align-items: center;
    justify-content: center;
    text-align: center;
    color: var(--white);
    font-weight: 600;
    font-size: 20px;
    line-height: 29px;
    letter-spacing: 0;
    white-space: nowrap;
  }
</style>
</head>
<body>
  <div class="banner">
    <div class="underwater-scene" role="img" aria-label="Snorkeler swimming in clear turquoise water on the left and a school of striped tropical fish on the right"></div>

    <div class="brand">
      <span class="brand-dot"></span>
      <span class="brand-name">VELMARO<small>TRIPS</small></span>
    </div>

    <div class="headline-badge"></div>
    <h1 class="headline">PRIVATE<br>BOAT CHARTERS IN<br>GRAND CAYMAN</h1>
  </div>
</body>
</html>
```